Content developers BC and Stationary
Nubra نبراس
Content developers BC and Stationary - Corporate Services
Creative Brief
Simple
Rana T alMuttairi
Creative Director
Jeddah
rana@nubraco.com
for second partner, with Arabic on the back: Khaled Naji خالد ناجي Managing Director المدير التنفيذي +966507213690 +٩٦٦٥٠٧٢١٣٦٩٠ k@nubraco.com
رنا طارق المطيري المدير الإبداعي +٩٦٦٥٠٨٤٤١٢٥٩ rana@nubraco.com
Concepts
Business Cards and Stationery for new compliance company.
Business Cards and Stationery for Background Check Company

```html
<!DOCTYPE html>
<html lang="en">
<head>
<meta charset="utf-8">
<title>Nubra Business Card</title>
<link rel="stylesheet" href="https://fonts.googleapis.com/css2?family=Montserrat:wght@400;500;600&family=Cairo:wght@400;700&display=swap">
<style>
  :root {
    --backdrop: #8c8c8e;
    --card: #ffffff;
    --violet: #9a5cc4;
    --violet-deep: #7d44ad;
    --indigo: #33348f;
    --indigo-soft: #5a4bb0;
    --ink-light: #ffffff;
  }
  html, body {
    margin: 0;
    width: 1200px;
    height: 818px;
    overflow: hidden;
    background: var(--backdrop);
    font-family: "Montserrat", sans-serif;
  }
  .stage { position: relative; width: 1200px; height: 818px; }
  .card {
    position: absolute;
    width: 560px;
    height: 320px;
    border-radius: 22px;
    background: var(--card);
    overflow: hidden;
    box-shadow: 0 6px 18px rgba(0,0,0,0.18);
  }
  .card-back { left: 150px; top: 110px; }
  .card-front { left: 490px; top: 390px; }

  .brand {
    position: absolute;
    display: flex;
    align-items: center;
    gap: 10px;
    color: var(--indigo);
    font-family: "Cairo", sans-serif;
    font-weight: 700;
    line-height: 1;
    white-space: nowrap;
  }
  .brand-mark {
    width: 14px; height: 14px;
    border-radius: 50%;
    background: var(--indigo);
  }
  .card-back .brand { left: 140px; top: 56px; font-size: 52px; }
  .card-front .brand { left: 36px; top: 44px; font-size: 40px; }

  .holder-ar {
    position: absolute;
    right: 40px;
    top: 160px;
    direction: rtl;
    text-align: right;
    font-family: "Cairo", sans-serif;
    color: var(--indigo);
  }
  .holder-ar-name { margin: 0; font-size: 20px; font-weight: 700; line-height: 1.3; }
  .holder-ar-role { margin: 0 0 10px; font-size: 12px; font-weight: 400; color: var(--violet-deep); }
  .holder-ar-line { margin: 0; font-size: 12px; line-height: 1.6; }
  .holder-ar-line.latin { direction: ltr; unicode-bidi: embed; font-family: "Montserrat", sans-serif; font-size: 11px; }

  .waves { position: absolute; inset: 0; width: 560px; height: 320px; }

  .holder {
    position: absolute;
    left: 30px;
    top: 222px;
    color: var(--ink-light);
  }
  .holder-name {
    margin: 0;
    font-size: 20px;
    font-weight: 500;
    letter-spacing: 0.5px;
    text-transform: uppercase;
  }
  .holder-role {
    margin: 4px 0 0;
    font-size: 9.5px;
    letter-spacing: 1px;
    text-transform: uppercase;
  }

  .contact {
    position: absolute;
    right: 24px;
    top: 168px;
    margin: 0;
    padding: 0;
    list-style: none;
    color: var(--ink-light);
    font-size: 10px;
    text-align: right;
  }
  .contact li {
    display: flex;
    justify-content: flex-end;
    align-items: center;
    gap: 8px;
    height: 17px;
  }
  .contact .address { display: block; height: auto; line-height: 1.35; margin-bottom: 10px; }
  .contact-icon { width: 10px; height: 10px; flex: none; }
</style>
</head>
<body>
<main class="stage">

  <section class="card card-back" aria-label="Card back">
    <div class="brand"><span class="brand-mark"></span><span>Nubra نبراس</span></div>
    <div class="holder-ar" lang="ar">
      <p class="holder-ar-name">خالد ناجي</p>
      <p class="holder-ar-role">المدير التنفيذي</p>
      <p class="holder-ar-line">+٩٦٦٥٠٧٢١٣٦٩٠</p>
      <p class="holder-ar-line latin">k@nubraco.com</p>
    </div>
  </section>

  <section class="card card-front" aria-label="Card front">
    <svg class="waves" viewBox="0 0 560 320" aria-hidden="true">
      <path d="M0 175 C140 150 300 100 560 95 L560 320 L0 320 Z" fill="var(--violet)"/>
      <path d="M120 168 C270 128 400 100 560 112" fill="none" stroke="var(--indigo)" stroke-width="7"/>
      <path d="M170 170 C300 138 420 118 560 128" fill="none" stroke="var(--indigo-soft)" stroke-width="4"/>
      <path d="M230 176 C340 150 440 136 560 142" fill="none" stroke="var(--indigo)" stroke-width="3"/>
      <path d="M0 188 C160 168 330 140 560 150" fill="none" stroke="var(--violet-deep)" stroke-width="2" opacity="0.6"/>
    </svg>

    <div class="brand"><span class="brand-mark"></span><span>Nubra نبراس</span></div>

    <div class="holder">
      <p class="holder-name">Khaled Naji</p>
      <p class="holder-role">Managing Director</p>
    </div>

    <ul class="contact">
      <li class="address">27 Corniche Road<br>Jeddah KSA</li>
      <li>+966507213690
        <svg class="contact-icon" viewBox="0 0 10 10"><path d="M2 1 L4 1 L4.5 3 L3.3 4 C4 5.5 4.5 6 6 6.7 L7 5.5 L9 6 L9 8 C5 8.5 1.5 5 2 1 Z" fill="#fff"/></svg></li>
      <li>+966507213690
        <svg class="contact-icon" viewBox="0 0 10 10"><rect x="3" y="0.5" width="4.5" height="9" rx="1" fill="#fff"/></svg></li>
      <li>+966507213690
        <svg class="contact-icon" viewBox="0 0 10 10"><rect x="1" y="2" width="8" height="6" rx="1" fill="#fff"/></svg></li>
      <li>k@nubraco.com
        <svg class="contact-icon" viewBox="0 0 10 10"><rect x="1" y="2" width="8" height="6" rx="0.8" fill="none" stroke="#fff" stroke-width="1.2"/><path d="M1.5 2.5 L5 5.5 L8.5 2.5" fill="none" stroke="#fff" stroke-width="1"/></svg></li>
      <li>www.nubraco.com
        <svg class="contact-icon" viewBox="0 0 10 10"><circle cx="5" cy="5" r="4.3" fill="#fff"/></svg></li>
    </ul>
  </section>

</main>
</body>
</html>
```